Business Stationery Design

I would like to get some stationery designed for my company. The stationery should include a letterhead, envelope, and business card. We are a technology consulting company specializing in Healthcare IT, and Education management systems. The colors of the stationery should match the logo. The logo is uploaded.

Target Market(s)

Hospitals, Clinics. Doctors offices. Private Schools.

Industry/Entity Type

Business

```html
<!DOCTYPE html>
<html lang="en">
<head>
<meta charset="utf-8">
<title>Sunmeadow Advisory Group – Stationery</title>
<link rel="stylesheet" href="https://fonts.googleapis.com/css2?family=Open+Sans:wght@400;600&display=swap">
<style>
:root{
  --green:#76c043;
  --yellow:#f4b400;
  --cream:#fbf0c9;
  --pale-green:#c9dfa0;
  --pale-yellow:#f6dd8e;
  --bg-from:#f5b800;
  --bg-to:#fbf1d2;
  --shadow:0 2px 5px rgba(120,80,0,.35);
}
*{margin:0;padding:0;box-sizing:border-box}
html,body{width:1200px;height:1200px;overflow:hidden}
body{
  position:relative;
  font-family:"Open Sans",Arial,sans-serif;
  background:linear-gradient(45deg,var(--bg-from) 0%,#f9d77a 50%,var(--bg-to) 100%);
}
.sheet{position:absolute;background:var(--cream);box-shadow:var(--shadow);overflow:hidden}

/* brand lockup */
.brand{display:flex;align-items:center;gap:4px;color:var(--green);font-weight:600;white-space:nowrap}
.brand-dot{border-radius:50%;background:var(--green);flex:none}
.brand.on-green{color:#fff}
.brand.on-green .brand-dot{background:#fff}
.tagline{color:var(--green);font-weight:400;white-space:nowrap}

/* letterhead */
.letterhead{left:238px;top:288px;width:349px;height:460px}
.letterhead .corner{position:absolute;right:0;top:0;width:84px;height:64px;background:var(--green);
  display:flex;flex-direction:column;align-items:center;justify-content:center}
.letterhead .corner .brand{font-size:9px}
.letterhead .corner .brand-dot{width:12px;height:12px}
.letterhead .corner .tagline{font-size:5px;color:#fff;margin-left:14px}
.letterhead .foot-bar{position:absolute;left:0;bottom:2px;width:12px;height:30px;background:var(--green)}
.letterhead .contact{position:absolute;left:17px;bottom:9px;font-size:6px;line-height:9px;color:var(--green)}
.letterhead .decor{position:absolute;right:6px;bottom:40px;width:80px;height:80px;border-radius:50%;background:var(--pale-yellow);opacity:.55}
.letterhead .ghost-name{position:absolute;right:8px;bottom:10px;font-size:18px;font-weight:400;color:var(--pale-green)}

/* envelopes */
.envelope-back{left:642px;top:340px;width:324px;height:154px}
.envelope-back svg{position:absolute;left:0;top:0}
.envelope-front{left:642px;top:548px;width:324px;height:154px}
.envelope-front .mark{position:absolute;left:18px;top:42px}
.envelope-front .brand{font-size:13px}
.envelope-front .brand-dot{width:15px;height:15px}
.envelope-front .tagline{font-size:6px;margin-left:19px}
.envelope-front .foot-bar{position:absolute;left:0;bottom:2px;width:10px;height:24px;background:var(--green)}
.envelope-front .contact{position:absolute;left:14px;bottom:9px;font-size:5px;line-height:7px;color:var(--green)}

/* business cards */
.card-front{left:428px;top:793px;width:197px;height:119px}
.card-front .mark{position:absolute;left:12px;top:50px}
.card-front .brand{font-size:11px}
.card-front .brand-dot{width:11px;height:11px}
.card-front .tagline{font-size:5px;margin-left:15px}
.card-front .divider{position:absolute;left:100px;top:32px;width:1px;height:42px;background:var(--yellow)}
.card-front .person{position:absolute;left:113px;top:32px;color:var(--green)}
.card-front .person .name{font-size:9.5px;line-height:11px}
.card-front .person .role{font-size:6px;color:var(--yellow);margin-bottom:2px}
.card-front .person ul{list-style:none;font-size:5px;line-height:7px}
.card-front .person li{display:flex;align-items:center;gap:3px}
.card-front .person svg{flex:none}
.card-front .bands{position:absolute;left:0;bottom:0}

.card-back{left:648px;top:793px;width:198px;height:119px;background:var(--green)}
.card-back .mark{position:absolute;left:66px;top:50px}
.card-back .brand{font-size:12px}
.card-back .brand-dot{width:12px;height:12px}
.card-back .tagline{font-size:5px;margin-left:16px;color:#fff}
.card-back .decor{position:absolute;left:132px;top:10px;width:60px;height:60px;border-radius:50%;background:rgba(255,255,255,.14)}
.card-back .ghost-name{position:absolute;right:6px;bottom:6px;font-size:13px;color:rgba(255,255,255,.25)}
</style>
</head>
<body>

<section class="sheet letterhead" aria-label="Letterhead">
  <div class="corner">
    <div class="brand on-green"><span class="brand-dot"></span>Sunmeadow</div>
    <div class="tagline">Advisory Group</div>
  </div>
  <div class="decor" role="img" aria-label="Faint tree emblem decoration"></div>
  <div class="ghost-name" aria-hidden="true">Sunmeadow</div>
  <div class="foot-bar"></div>
  <div class="contact">Full Address, FA 01, City Country | 0123 456 7890<br>info@yourbusiness.com | www.yourbusiness.com</div>
</section>

<section class="sheet envelope-back" aria-label="Envelope back">
  <svg width="324" height="154" viewBox="0 0 324 154" aria-hidden="true">
    <polygon points="0,0 324,0 324,2 300,28 24,28 0,2" fill="var(--green)"/>
    <circle cx="162" cy="12" r="4" fill="#fff"/>
  </svg>
</section>

<section class="sheet envelope-front" aria-label="Envelope front">
  <div class="mark">
    <div class="brand"><span class="brand-dot"></span>Sunmeadow</div>
    <div class="tagline">Advisory Group</div>
  </div>
  <div class="foot-bar"></div>
  <div class="contact">Full Address, FA 01, City Country | 0123 456 7890<br>info@yourbusiness.com | www.yourbusiness.com</div>
</section>

<section class="sheet card-front" aria-label="Business card front">
  <div class="mark">
    <div class="brand"><span class="brand-dot"></span>Sunmeadow</div>
    <div class="tagline">Advisory Group</div>
  </div>
  <div class="divider"></div>
  <div class="person">
    <div class="name">Your Name</div>
    <div class="role">CEO</div>
    <ul>
      <li><svg width="5" height="6" viewBox="0 0 10 12"><path d="M5 0a4 4 0 0 1 4 4c0 3-4 8-4 8S1 7 1 4a4 4 0 0 1 4-4z" fill="var(--green)"/></svg>Full Address, FA 01</li>
      <li style="padding-left:8px">City Country</li>
      <li><svg width="5" height="5" viewBox="0 0 10 10"><path d="M2 0l2 2-1 2 3 3 2-1 2 2-2 2C4 10 0 6 0 2z" fill="var(--green)"/></svg>0123 456 789</li>
      <li><svg width="5" height="5" viewBox="0 0 10 10"><circle cx="5" cy="5" r="5" fill="var(--green)"/></svg>info@yourbusiness.com</li>
      <li><svg width="5" height="5" viewBox="0 0 10 10"><circle cx="5" cy="5" r="4" fill="none" stroke="var(--green)" stroke-width="2"/></svg>www.yourbusiness.com</li>
    </ul>
  </div>
  <svg class="bands" width="197" height="12" viewBox="0 0 197 12" aria-hidden="true">
    <polygon points="90,3 197,3 197,5 92,5" fill="var(--yellow)"/>
    <polygon points="0,6 94,6 100,12 0,12" fill="var(--green)"/>
    <polygon points="102,7 197,7 197,12 107,12" fill="var(--green)"/>
  </svg>
</section>

<section class="sheet card-back" aria-label="Business card back">
  <div class="decor" role="img" aria-label="Faint tree emblem decoration"></div>
  <div class="ghost-name" aria-hidden="true">Sunmeadow</div>
  <div class="mark">
    <div class="brand on-green"><span class="brand-dot"></span>Sunmeadow</div>
    <div class="tagline">Advisory Group</div>
  </div>
</section>

</body>
</html>
```